Business Card Design Project

We require business cards for "Venoth". We are composed of elite prior military personnel. Our goal is to provide site security for premium businesses who want on the most professional of agents on their premises. Additionally, we will provide executive protection for individuals who require professionalism, flexibility, and dedication

We want this business card to communicate professionalism, dependability, strength. However, we are not an overtly tactical agency and do not want to intimidate our clients personnel or their client. We want to give them a sense of security.
Updates

At the request of one of the designers I've listed the appropriate text that should appear on the card. Please feel free to arrange it in a creative and professional manor.

I've also uploaded a .png file of the triangle logo with no text. Please feel free to incorporate this into your designs.

ThanksĀ 

Target Market(s)

Premium businesses, executives, celebrities, and governments.

Industry/Entity Type

Security

Requirements
Must have
• Text Info that will go on the card. It does not have to be in this order:
Name
Title
Office Phone Number
Cell Phone Number
Email
Website
Mailing Address
Nice to have
• On the back I'd like to see the triangle portion of the logo displayed in a creative way that leaves enough room to write down information if needed.
Should not have
• - Weapons, Globes, or Shields. Every rent-a-cop company has that, and that's not what we are.

```html
<!DOCTYPE html>
<html lang="en">
<head>
<meta charset="UTF-8">
<title>Venoth — Business Card</title>
<link href="https://fonts.googleapis.com/css2?family=Quicksand:wght@400;500;700&display=swap" rel="stylesheet">
<style>
  :root {
    --ink-dark: #333333;
    --ink-body: #2b2b2b;
    --brand-blue: #2f86d6;
    --blue-light: #1f8bd0;
    --blue-deep: #0b4a8e;
    --paper-light: #fafafa;
    --paper-mid: #d9d9d9;
    --paper-edge: #bdbdbd;
    --divider: #111111;
    --white: #ffffff;
  }
  html, body {
    margin: 0;
    padding: 0;
    overflow: hidden;
    background: var(--white);
  }
  .canvas {
    position: relative;
    width: 1050px;
    height: 1200px;
    overflow: hidden;
    font-family: "Quicksand", sans-serif;
  }
  .card-front {
    position: absolute;
    left: 0; top: 0;
    width: 1050px; height: 600px;
    background: radial-gradient(ellipse 520px 420px at 470px 230px, var(--paper-light) 0%, var(--paper-mid) 70%, var(--paper-edge) 100%);
  }
  .front-panel {
    position: absolute;
    left: 0; top: 0;
  }
  .front-wordmark {
    position: absolute;
    left: 22px; top: 18px;
    margin: 0;
    font-size: 104px;
    font-weight: 700;
    letter-spacing: 4px;
    color: var(--ink-dark);
    line-height: 1;
  }
  .front-tagline {
    position: absolute;
    left: 8px; top: 156px;
    margin: 0;
    font-size: 24px;
    font-weight: 500;
    color: var(--ink-body);
  }
  .front-contact {
    position: absolute;
    right: 20px; top: 470px;
    margin: 0;
    text-align: right;
    font-size: 37px;
    line-height: 38px;
    font-weight: 500;
    color: var(--white);
    letter-spacing: 1px;
  }
  .card-divider {
    position: absolute;
    left: 0; top: 599px;
    width: 1050px; height: 3px;
    background: var(--divider);
  }
  .card-back {
    position: absolute;
    left: 0; top: 602px;
    width: 1050px; height: 598px;
    background: radial-gradient(ellipse 560px 460px at 525px 260px, var(--paper-light) 0%, var(--paper-mid) 70%, var(--paper-edge) 100%);
  }
  .back-heading {
    position: absolute;
    left: 0; top: 44px;
    width: 1050px;
    margin: 0;
    text-align: center;
    font-size: 45px;
    line-height: 48px;
    font-weight: 500;
    letter-spacing: 2px;
    color: var(--brand-blue);
  }
  .service-list {
    position: absolute;
    left: 0; top: 200px;
    margin: 0; padding: 0;
    list-style: none;
  }
  .service-item {
    position: relative;
    height: 70px;
    padding-left: 233px;
    font-size: 36px;
    line-height: 56px;
    letter-spacing: 1px;
    color: var(--ink-body);
    white-space: nowrap;
  }
  .service-item::before {
    content: "";
    position: absolute;
    left: 25px; top: 27px;
    width: 193px; height: 2px;
    background: var(--brand-blue);
  }
  .back-wordmark {
    position: absolute;
    left: 0; top: 508px;
    width: 1050px;
    margin: 0;
    text-align: center;
    font-size: 50px;
    font-weight: 700;
    letter-spacing: 2px;
    color: var(--ink-dark);
    line-height: 1;
  }
</style>
</head>
<body>
<main class="canvas">
  <section class="card-front">
    <svg class="front-panel" width="1050" height="600" viewBox="0 0 1050 600" aria-hidden="true">
      <defs>
        <radialGradient id="panelBlue" cx="610" cy="300" r="520" gradientUnits="userSpaceOnUse">
          <stop offset="0" stop-color="var(--blue-light)" style="stop-color:#1f8bd0"/>
          <stop offset="1" stop-color="#0b4a8e"/>
        </radialGradient>
      </defs>
      <polygon points="195,600 825,0 1050,0 1050,600" fill="url(#panelBlue)"/>
    </svg>
    <h1 class="front-wordmark">VENOTH</h1>
    <p class="front-tagline">Providing site security for premium businesses.</p>
    <p class="front-contact">Contact Information Here<br>Phone Number<br>Website</p>
  </section>

  <div class="card-divider"></div>

  <section class="card-back">
    <h2 class="back-heading">Providing site security for<br>premium businesses</h2>
    <ul class="service-list">
      <li class="service-item">Composed of elite prior military personnel</li>
      <li class="service-item">Professional agents on premises</li>
      <li class="service-item">Executive protection for indivduals</li>
    </ul>
    <p class="back-wordmark">VENOTH</p>
  </section>
</main>
</body>
</html>
```